Clinique VeraNova business card

I am looking for a talented designer who can an existing design and make it better. I need a 2 sided business card to represent our Psychology clinic staff members. It would need to be elegant, yet modern, clean, light and uplifting. Simple design, quick turnaround time. Lots of files and logos to use as your guide. I hope to hear from you!

Target Market(s)

Clients who receive the card of our therapists

Industry/Entity Type

Health And Wellness

Contact Information for Business Card

Following the similar designs of the Maplebrook Care Center card, there will be 2 sides. Side 1 (front) should have the veranova logo instead of the maplebrook care logo, The title should read Clinique VeraNova instead of centre Bien-Être Mésange/Maplebrook care Center.

Side 2 should have a spiral similar to the one on the card with sunflower leaves, and the title of the Therapist should be Marielle Odile Brunet, Psychologue, Psychologist, her email: Marielle@Veranova-example.com and phone number should be (514) 555-0137

Font styles to use
Serif

Colors
fee18a
85cae6
ffffff
0255a3

Requirements
Must have
• Side 1 (front): veranova logo- Name of the clinic, clinic address, contact info of clinic etc. use little icons in front of each (just like on sample card)
side 2: Therapist name titles and their contact info underneath with design of spiral and/or sunflower leaves..
Nice to have
• soft colors along soft yellow/gold and blue like the logo,
mini icons for phone, email, address etc.
We do work with a holistic, zen approach so it should represent that to some extent

```html
<!DOCTYPE html>
<html lang="fr">
<head>
<meta charset="utf-8">
<title>Clinique VeraNova – cartes professionnelles</title>
<link rel="stylesheet" href="https://fonts.googleapis.com/css2?family=Roboto:wght@400;700&display=swap">
<style>
  :root {
    --backdrop: #b8b8b8;
    --card: #ffffff;
    --ink: #231f5c;
    --text: #2a2a3a;
    --sun: #fdd321;
    --sun-deep: #f5a623;
    --rule: #8a88a8;
  }
  * { box-sizing: border-box; margin: 0; padding: 0; }
  html, body { width: 1200px; height: 801px; overflow: hidden; }
  body {
    background: var(--backdrop);
    font-family: "Roboto", Arial, sans-serif;
    position: relative;
  }
  .card {
    position: absolute;
    top: 274px;
    width: 443px;
    height: 263px;
    background: var(--card);
    overflow: hidden;
  }
  .card--front { left: 153px; }
  .card--back { left: 625px; }

  /* Front */
  .brand {
    position: absolute;
    left: 26px;
    top: 104px;
    display: flex;
    align-items: center;
    gap: 8px;
  }
  .brand__dot {
    width: 30px; height: 30px;
    border-radius: 50%;
    background: var(--sun);
  }
  .brand__name {
    font-size: 34px;
    font-weight: 400;
    color: var(--ink);
    letter-spacing: 0.2px;
  }
  .divider {
    position: absolute;
    left: 226px; top: 59px;
    width: 1px; height: 145px;
    background: var(--rule);
  }
  .clinic-name {
    position: absolute;
    left: 235px; top: 59px;
    font-size: 18px;
    font-weight: 700;
    color: var(--ink);
  }
  .contact {
    position: absolute;
    list-style: none;
    font-size: 12.6px;
    color: var(--text);
    line-height: 16px;
  }
  .contact li { display: flex; align-items: flex-start; gap: 4px; }
  .contact svg { width: 12px; height: 12px; margin-top: 2px; flex: none; fill: var(--ink); }
  .contact--clinic { left: 235px; top: 90px; }
  .contact--clinic .gap { margin-top: 9px; }
  .contact--clinic .gap-lg { margin-top: 11px; }

  /* Back */
  .sunburst {
    position: absolute;
    left: -4px; top: 2px;
    width: 256px; height: 256px;
    border-radius: 50%;
    background: radial-gradient(circle at 50% 50%, var(--sun-deep) 0%, #f8c12a 38%, var(--sun) 62%, #fde47a 100%);
  }
  .therapist-name {
    position: absolute;
    left: 263px; top: 82px;
    font-size: 18px;
    font-weight: 700;
    color: var(--ink);
  }
  .therapist-title {
    position: absolute;
    left: 263px; top: 104px;
    font-size: 12.6px;
    color: var(--text);
  }
  .contact--therapist { left: 261px; top: 145px; }
</style>
</head>
<body>

<section class="card card--front" aria-label="Recto">
  <div class="brand">
    <span class="brand__dot"></span>
    <span class="brand__name">VeraNova</span>
  </div>
  <div class="divider"></div>
  <h1 class="clinic-name">Clinique VeraNova</h1>
  <ul class="contact contact--clinic">
    <li><svg viewBox="0 0 24 24"><path d="M6.6 10.8a15.1 15.1 0 0 0 6.6 6.6l2.2-2.2c.3-.3.7-.4 1-.2 1.1.4 2.3.6 3.6.6.6 0 1 .4 1 1V20c0 .6-.4 1-1 1A17 17 0 0 1 3 4c0-.6.4-1 1-1h3.5c.6 0 1 .4 1 1 0 1.3.2 2.5.6 3.6.1.3 0 .7-.2 1z"/></svg>514- 555-0137</li>
    <li><svg viewBox="0 0 24 24"><path d="M2 5h20v14H2zm2 2v.5l8 5 8-5V7zm0 3v7h16v-7l-8 5z"/></svg>info@veranova.com</li>
    <li><svg viewBox="0 0 24 24"><path d="M12 2a10 10 0 1 0 0 20 10 10 0 0 0 0-20zm0 2c.9 1.2 1.6 2.6 2 4h-4c.4-1.4 1.1-2.8 2-4zM4.3 14a8 8 0 0 1 0-4h3.3a16 16 0 0 0 0 4zm.8 2h3a12 12 0 0 0 1.4 3.6A8 8 0 0 1 5.1 16zm3-8h-3a8 8 0 0 1 4.4-3.6C8.9 5.5 8.4 6.7 8.1 8zM12 20c-.9-1.2-1.6-2.6-2-4h4c-.4 1.4-1.1 2.8-2 4zm2.3-6H9.7a14 14 0 0 1 0-4h4.6a14 14 0 0 1 0 4zm.2 5.6c.6-1.1 1.1-2.3 1.4-3.6h3a8 8 0 0 1-4.4 3.6zm1.9-5.6a16 16 0 0 0 0-4h3.3a8 8 0 0 1 0 4zm-.5-6c-.3-1.3-.8-2.5-1.4-3.6A8 8 0 0 1 18.9 8z"/></svg>www.veranova.com</li>
    <li class="gap"><svg viewBox="0 0 24 24"><rect x="2" y="2" width="20" height="20" rx="2"/></svg>www.social-link.example/Veranova</li>
    <li class="gap-lg"><svg viewBox="0 0 24 24"><path d="M12 2a7 7 0 0 0-7 7c0 5 7 13 7 13s7-8 7-13a7 7 0 0 0-7-7zm0 9.5A2.5 2.5 0 1 1 12 6.5a2.5 2.5 0 0 1 0 5z"/></svg><span>4410 boul. des Érables ouest<br>Saint-Aurèle, Qc., J9X 2K4</span></li>
  </ul>
</section>

<section class="card card--back" aria-label="Verso">
  <div class="sunburst" role="img" aria-label="Illustration d'un tournesol jaune aux pétales rayonnants avec une spirale orange au centre"></div>
  <h2 class="therapist-name">Marielle Odile Brunet</h2>
  <p class="therapist-title">Psychologue, Psychologist</p>
  <ul class="contact contact--therapist">
    <li><svg viewBox="0 0 24 24"><path d="M6.6 10.8a15.1 15.1 0 0 0 6.6 6.6l2.2-2.2c.3-.3.7-.4 1-.2 1.1.4 2.3.6 3.6.6.6 0 1 .4 1 1V20c0 .6-.4 1-1 1A17 17 0 0 1 3 4c0-.6.4-1 1-1h3.5c.6 0 1 .4 1 1 0 1.3.2 2.5.6 3.6.1.3 0 .7-.2 1z"/></svg>(514) 555-0137</li>
    <li><svg viewBox="0 0 24 24"><path d="M2 5h20v14H2zm2 2v.5l8 5 8-5V7zm0 3v7h16v-7l-8 5z"/></svg>Marielle@Veranova-example.com</li>
  </ul>
</section>

</body>
</html>
```